Laser Hair Removal Tri Fold brochure

I'm looking for a tri fold brochure (A4 size) for a cosmetic surgery centre / dermatology clinic for our laser hair removal services please.

Whilst we are more medical centre than spa, and cater to both men and women, some warmth would good to convey.

I've attached several versions of our logo - either can be used depending on the design style and colouring used. You can see more about us at www.quellmira.ae. I've also added some photos of our clinic if that is of any interest. No need to use them but they're there if you want them.

As we are based in the Middle East, no images showing too much skin should be used. Legs or face, or certain parts of the body are fine, so long as they aren't too revealing, as we need to be culturally sensitive.

One of our (non creative) staff has drafted a basic brochure using Word, which I've attached as a point of reference or for content, although naturally it's not professionally done so it's by no means a design guide! Also open to written content improvement if necessary but this part is non-essential. The only content I specifically want to keep is the price list please.

Many thanks!

Industry/Entity Type

Clinic

```html
<!DOCTYPE html>
<html lang="en">
<head>
<meta charset="utf-8">
<title>Laser Hair Removal – Quellmira Clinic Brochure</title>
<link href="https://fonts.googleapis.com/css2?family=Didact+Gothic&family=Montserrat:wght@600;700&display=swap" rel="stylesheet">
<style>
  :root {
    --purple-deep: #4a0f6b;
    --purple-mid: #7a2a9c;
    --purple-text: #5b1c7c;
    --lavender-ring: #c9a6dc;
    --panel-bg: #dde3e3;
    --divider: #5a1580;
    --heading: #141414;
    --footer-dark: #1b1420;
  }
  html, body { margin: 0; padding: 0; overflow: hidden; }
  body { width: 1200px; height: 933px; background: #fff; }
  .brochure {
    position: relative; width: 1200px; height: 933px; overflow: hidden;
    background: var(--panel-bg);
    font-family: "Didact Gothic", "Century Gothic", sans-serif;
    color: var(--purple-text);
  }
  .top-band {
    position: absolute; left: 0; top: 0; width: 1200px; height: 125px;
    background: radial-gradient(ellipse at 50% 60%, var(--purple-mid), var(--purple-deep) 75%);
  }
  .bottom-band {
    position: absolute; left: 0; top: 875px; width: 1200px; height: 58px;
    background: linear-gradient(to bottom, var(--footer-dark), #2c1a36 70%, #3a1650);
  }
  .divider {
    position: absolute; top: 0; width: 10px; height: 933px; background: var(--divider);
  }
  .divider--one { left: 395px; }
  .divider--two { left: 783px; }
  .photo {
    position: absolute; border-radius: 50%; box-sizing: border-box;
  }
  .photo--lounge { left: -10px; top: -30px; width: 134px; height: 134px; border: 8px solid var(--lavender-ring);
    background: radial-gradient(circle at 40% 50%, #8a6a4a, #3c2a1e); }
  .photo--salon { left: 330px; top: 28px; width: 140px; height: 140px; border: 10px solid var(--lavender-ring);
    background: radial-gradient(circle at 45% 40%, #c89a6a, #5a2e1a); }
  .photo--treatment { left: 718px; top: -40px; width: 142px; height: 142px; border: 10px solid var(--lavender-ring);
    background: radial-gradient(circle at 50% 50%, #b0542a, #3a1a10); }
  .photo--building { left: 1025px; top: -20px; width: 180px; height: 180px; border: 12px solid #ece4f0;
    background: linear-gradient(to bottom, #9cc4e4, #e8eef2 60%, #8a9a88); }
  h2 {
    font-family: "Montserrat", "Helvetica", sans-serif; font-weight: 600;
    color: var(--heading); margin: 0; letter-spacing: 1.5px;
  }
  .body-copy {
    position: absolute; margin: 0; font-size: 13.6px; line-height: 22px;
    letter-spacing: 1.4px; text-align: justify;
  }
  .body-copy p { margin: 0 0 22px; }
  .why-heading { position: absolute; left: 25px; top: 170px; font-size: 15.5px; }
  .why-copy { left: 25px; top: 214px; width: 350px; }
  .remove-heading { position: absolute; left: 420px; top: 170px; width: 348px; text-align: right; font-size: 15.5px; line-height: 21px; }
  .remove-copy { left: 422px; top: 244px; width: 350px; }
  .cycles-heading { position: absolute; left: 420px; top: 499px; width: 348px; text-align: right; font-size: 15.5px; line-height: 22px; }
  .cycles-copy { left: 422px; top: 552px; width: 350px; }
  .results-heading { position: absolute; left: 600px; top: 739px; width: 168px; text-align: right; font-size: 15.5px; line-height: 22px; }
  .result-photo { position: absolute; background: linear-gradient(135deg, #b5bcc0, #d9c6b0 50%, #a99a8c); }
  .result-photo--large { left: 422px; top: 744px; width: 118px; height: 118px; }
  .result-photo--small { left: 563px; top: 790px; width: 107px; height: 72px; }
  .advantages-heading { position: absolute; left: 806px; top: 171px; font-size: 18.5px; line-height: 22px; letter-spacing: 2px; }
  .advantages { position: absolute; left: 0; top: 0; margin: 0; padding: 0; list-style: none; font-size: 16.5px; letter-spacing: 1.3px; line-height: 22px; }
  .advantages li { position: absolute; white-space: nowrap; padding-left: 16px; }
  .advantages li::before { content: ""; position: absolute; left: 0; top: 7px; width: 8px; height: 8px; border-radius: 50%; background: var(--heading); }
  .expert-heading { position: absolute; left: 806px; top: 505px; font-size: 19px; letter-spacing: 2px; }
  .portrait { position: absolute; left: 816px; top: 538px; width: 124px; height: 124px; border-radius: 50%; box-sizing: border-box;
    border: 9px solid var(--purple-mid); background: radial-gradient(circle at 50% 45%, #d8b8a0, #6a6a70 70%); }
  .expert-name { position: absolute; left: 962px; top: 578px; font-size: 16px; line-height: 22px; letter-spacing: 1.4px; }
  .expert-copy { left: 812px; top: 670px; width: 363px; }
</style>
</head>
<body>
<main class="brochure">
  <div class="top-band"></div>
  <div class="bottom-band"></div>
  <div class="divider divider--one"></div>
  <div class="divider divider--two"></div>

  <div class="photo photo--lounge" role="img" aria-label="Clinic waiting lounge"></div>
  <div class="photo photo--salon" role="img" aria-label="Clinic treatment chairs"></div>
  <div class="photo photo--treatment" role="img" aria-label="Laser treatment room"></div>
  <div class="photo photo--building" role="img" aria-label="Exterior of the Quellmira clinic building"></div>

  <section class="panel panel--why">
    <h2 class="why-heading">Why choose Laser hair removal?</h2>
    <div class="body-copy why-copy">
      <p>Almost our entire body is covered with hair. Most of it is fine and pale, however we almost all have darker, coarse hair in places we wouldn’t want or expect. It may be a question of aesthetics or hygiene; in any case, this excess body hair is considered as embarrassing and bothersome, especially in places like legs, bikini line, neck, arms and armpits, chest and back.</p>
      <p>Laser hair removal is becoming more and more mainstream with women as well as men; it is one of the most popular aesthetic treatments in practices all over the world. No one really wants to have more discomfort, ingrown hair and irritated or infected skin, which is the usual consequence of shaving, plucking, waxing... and it has to be repeated over and over again. Laser hair removal is a long-lasting, comfortable solution!</p>
      <p>Laser hair removal is a much faster and more efficient procedure than most other available treatments. Laser light targets hair follicles and eliminates or significantly impedes hair from growing back.</p>
    </div>
  </section>

  <section class="panel panel--method">
    <h2 class="remove-heading">Remove unwanted hair quickly and more effectively with laser hair removal</h2>
    <div class="body-copy remove-copy">
      <p>The deep penetration of Nd:YAG laser ensures it reaches even the deepest follicles, while its low absorption in all skin types ensures the surrounding tissue is preserved. This guarantees safe, fast and effective hair removal, even in the darkest skin types, without the epidermal damage other light-based treatments inherently cause. The procedure is quick and largely pain-free. You will be able to return to your normal activities immediately.</p>
    </div>
    <h2 class="cycles-heading">Because Hair Grows<br>in Cycles</h2>
    <div class="body-copy cycles-copy">
      <p>Because hair grows in cycles, it takes several treatments for it’s complete removal. The outcome also depends on hair quality and the quantity of hair follicles, along with the metabolism and hormonal level of each single individual. As a guide, however, four to six treatments are usually all that are required to effectively remove all the hair.</p>
    </div>
    <h2 class="results-heading">Before &amp; After<br>Results</h2>
    <div class="result-photo result-photo--large" role="img" aria-label="Before and after skin comparison photos"></div>
    <div class="result-photo result-photo--small" role="img" aria-label="Before and after skin comparison photos"></div>
  </section>

  <section class="panel panel--advantages">
    <h2 class="advantages-heading">Advantages of<br>Laser hair removal</h2>
    <ul class="advantages">
      <li style="left:805px;top:252px">Safe &amp; Effective</li>
      <li style="left:825px;top:287px">Fast &amp; Convenient</li>
      <li style="left:845px;top:323px">Suitable for All Skin Types</li>
      <li style="left:866px;top:360px">No Pain, No Ingrown hair or<br>Infected Skin</li>
      <li style="left:895px;top:415px">Suitable for Larger and<br>Smaller Areas</li>
    </ul>
    <h2 class="expert-heading">OUR EXPERT</h2>
    <div class="portrait" role="img" aria-label="Portrait of the clinic dermatologist"></div>
    <h2 class="expert-name">Dr Lukas Hartmann<br>DERMATOLOGIST</h2>
    <div class="body-copy expert-copy">
      <p>Dr Lukas Hartmann is a German Board certified in Dermatology and Allergy. His main areas of expertise are aesthetic medicine procedures and the treatment of skin cancer, including surgeries, as well as laser &amp; light applications such as photodynamic therapy. He is also an expert in diagnosis and treatment of allergies, and he enjoys solving complex dermatological cases.</p>
    </div>
  </section>
</main>
</body>
</html>
```